Quillmere business card

We're looking to "refresh" our original Quillmere logo design and also get a new business card design. We're a modern consulting and software business that's been around 4-years now. We work with large professional companies and therefore require a design that is simple and professional. We would like to retain the notch in the "A" and just the word "Quillmere" as the logo. We like greys, silvers, black, white...but happy to explore highlight color. We're looking for understated modern.

Industry/Entity Type

Software

```html
<!DOCTYPE html>
<html lang="en">
<head>
<meta charset="utf-8">
<title>Quillmere business card</title>
<link rel="stylesheet" href="https://fonts.googleapis.com/css2?family=Barlow:wght@500;600&display=swap">
<style>
  :root {
    --backdrop: #ffcb0a;
    --card-dark: #414141;
    --card-light: #ffffff;
    --ink: #3f3f3f;
    --accent: #ffcb0a;
    --shadow: rgba(60, 40, 0, 0.45);
  }
  html, body {
    margin: 0;
    padding: 0;
    width: 1200px;
    height: 1000px;
    overflow: hidden;
  }
  body {
    background: var(--backdrop);
    position: relative;
    font-family: "Barlow", Arial, sans-serif;
  }
  .card {
    position: absolute;
    width: 630px;
    height: 359px;
    box-shadow: 4px 6px 9px var(--shadow);
  }
  .card-front {
    left: 97px;
    top: 94px;
    background: var(--card-dark);
  }
  .wordmark {
    position: absolute;
    right: 47px;
    top: 212px;
    margin: 0;
    font-size: 76px;
    font-weight: 500;
    line-height: 1;
    letter-spacing: -1px;
    color: #ffffff;
  }
  .card-back {
    left: 443px;
    top: 516px;
    height: 360px;
    background: var(--card-light);
    color: var(--ink);
  }
  .contact {
    position: absolute;
    left: 51px;
    top: 139px;
    margin: 0;
  }
  .person-name {
    font-size: 22px;
    font-weight: 500;
    line-height: 30px;
    margin: 0;
  }
  .person-title {
    font-size: 20px;
    font-weight: 500;
    line-height: 30px;
    margin: 0 0 37px;
  }
  .details {
    font-size: 18px;
    font-weight: 500;
    line-height: 24.5px;
    margin: 0;
    font-style: normal;
  }
  .pointer {
    display: inline-block;
    width: 11px;
    height: 9px;
    margin: 0 2px 0 3px;
    vertical-align: 2px;
  }
  .gap { margin-left: 8px; }
</style>
</head>
<body>
  <section class="card card-front">
    <p class="wordmark">Quillmere</p>
  </section>

  <section class="card card-back">
    <div class="contact">
      <p class="person-name">Your Name</p>
      <p class="person-title">Title</p>
      <address class="details">
        Address Line 1<br>
        Address Line 1<br>
        Tel<svg class="pointer" viewBox="0 0 11 9" aria-hidden="true"><polygon points="0,0 11,4.5 0,9" fill="var(--accent)"/></svg>0123456789<span class="gap">Fax</span><svg class="pointer" viewBox="0 0 11 9" aria-hidden="true"><polygon points="0,0 11,4.5 0,9" fill="var(--accent)"/></svg>0123456789<br>
        mail@website.com<span class="gap">www.website.com</span>
      </address>
    </div>
  </section>
</body>
</html>
```